Business Card for New Business

Please design a business card using our logo and font files. This is only one card for one person, as listed in details section.

Industry/Entity Type

Business

Contact Information for Business Card

Carl Voserby

Phone 240.318.6624
Cell 703.581.4096
Email carl@moltravex.com

www.moltravex.com

Address
18250 Brennick Lane #314
Damascus, MD 20715

Font styles to use
Sans Serif

Requirements
Must have
• Information listed in detail section. Must be standard card size.

```html
<!DOCTYPE html>
<html lang="en">
<head>
<meta charset="utf-8">
<title>Moltravex Productions — Business Card</title>
<link rel="stylesheet" href="https://fonts.googleapis.com/css2?family=Questrial&display=swap">
<style>
  :root {
    --bg: #e6e6e6;
    --card: #ffffff;
    --orange: #d65a1f;
    --red: #c93a35;
    --ink: #3a3a3a;
    --muted: #555555;
  }
  * { margin: 0; padding: 0; box-sizing: border-box; }
  html, body {
    width: 1200px; height: 900px; overflow: hidden;
    background: var(--bg);
    font-family: "Questrial", "Century Gothic", sans-serif;
  }
  .card {
    position: absolute; left: 180px; top: 210px;
    width: 840px; height: 480px;
    background: var(--card);
    border-radius: 28px;
    overflow: hidden;
    box-shadow: 0 10px 30px rgba(0,0,0,0.18);
  }
  .card__band { position: absolute; left: 0; bottom: 0; width: 840px; height: 36px; }

  .brand {
    position: absolute; left: 90px; top: 240px;
    display: flex; align-items: center; gap: 14px;
  }
  .brand__dot { width: 26px; height: 26px; border-radius: 50%; background: var(--orange); flex: none; }
  .brand__name {
    font-size: 34px; font-weight: 400; color: var(--orange);
    line-height: 1; white-space: nowrap;
  }

  .contact { position: absolute; left: 500px; top: 100px; color: var(--ink); }
  .contact__name { font-size: 34px; font-weight: 400; color: var(--red); line-height: 1; }
  .contact__role { font-size: 14px; color: var(--muted); margin-top: 4px; letter-spacing: 0.5px; }
  .contact__list { list-style: none; margin-top: 20px; }
  .contact__item { display: flex; align-items: center; gap: 14px; font-size: 15px; height: 26px; letter-spacing: 0.5px; }
  .contact__icon { width: 16px; height: 16px; fill: none; stroke: var(--red); stroke-width: 1.8; flex: none; }
  .contact__address { margin-top: 14px; font-size: 15px; font-style: normal; line-height: 1.45; letter-spacing: 0.5px; padding-left: 30px; }
</style>
</head>
<body>
  <article class="card">
    <div class="brand">
      <span class="brand__dot"></span>
      <span class="brand__name">Moltravex Productions</span>
    </div>

    <section class="contact">
      <h1 class="contact__name">Carl Voserby</h1>
      <p class="contact__role">Managing Director</p>
      <ul class="contact__list">
        <li class="contact__item">
          <svg class="contact__icon" viewBox="0 0 16 16"><path d="M3 2h3l1 4-2 1c1 2 2 3 4 4l1-2 4 1v3c-6 1-12-5-11-11z"/></svg>
          240.318.6624
        </li>
        <li class="contact__item">
          <svg class="contact__icon" viewBox="0 0 16 16"><rect x="4.5" y="1.5" width="7" height="13" rx="1.5"/><line x1="7" y1="12" x2="9" y2="12"/></svg>
          703.581.4096
        </li>
        <li class="contact__item">
          <svg class="contact__icon" viewBox="0 0 16 16"><rect x="1.5" y="3.5" width="13" height="9"/><path d="M1.5 3.5l6.5 5 6.5-5"/></svg>
          carl@moltravex.com
        </li>
        <li class="contact__item">
          <svg class="contact__icon" viewBox="0 0 16 16"><circle cx="8" cy="8" r="6.5"/><ellipse cx="8" cy="8" rx="2.8" ry="6.5"/><line x1="1.5" y1="8" x2="14.5" y2="8"/></svg>
          www.moltravex.com
        </li>
      </ul>
      <address class="contact__address">
        18250 Brennick Lane #314<br>
        Damascus, MD 20715
      </address>
    </section>

    <svg class="card__band" viewBox="0 0 840 36" preserveAspectRatio="none" aria-hidden="true">
      <polygon points="0,0 522,0 514,36 0,36" fill="var(--orange)"/>
      <polygon points="530,0 840,0 840,36 522,36" fill="var(--red)"/>
    </svg>
  </article>
</body>
</html>
```